Broschüre für Immobilienvertrieb
Zielgruppe
Wir sind ein Immobilienvertrieb im Bereich Neubau-Immobilien und Bestand-Immobilien aus München. Die Firma BLOR existiert seit über 30 Jahren. Vor 4 Jahren haben wir ein cooles modernes Rebranding durchgeführt, sodass man mit unserem neuen Corporate Design richtig Spaß am Gestalten haben kann.
Eine konkrete Zielgruppe zu definieren ist schwierig, da unsere Käufer von 20-80 Jahren sein können. Ob junge, erfolgreiche Menschen, junge Familien, ältere Erwachsene, die von sich nach Auszug ihrer Kinder von ihrem Haus trennen wollen und eine kleinere Wohnung suchen oder einfach der Kapitalanleger, der auf der Suche nach einer neuen Investition ist.
Unsere CI ist gradlinig und setzt sich aus anthrazit, neonorange und weiß zusammen (Styleguide ist anbei).
Im Bestand gibt es nicht pro Objekt ein CI, hier wird mit dem der BLOR gearbeitet. Im Neubau hat jedes einzelne Projekt sein eigenes CI (siehe aktuell hausfeld-neu.de).
www.blor.de
Aufgabenstellung
Zur Aufgabe: Für die Bestandimmobilien benötigen wir ein neues Layout eines Immobilienexposé. Das Exposé wird sowohl online verwendet als auch von uns selbst gedruckt und gebunden.
Input: beigefügt ein Beispielexposé - grundsätzlich gefällt uns das Design, wir möchten jedoch etwas NEUES, modernes. Bitte keine Kopien des alten Exposés, dies soll nur als Input dienen (gerne können die Daten der Wohnung für den neuen Designentwurf genutzt werden).
Die Datei soll von uns befüllbar sein, sodass wir Texte und Bilder selbst austauschen können.
Für die Onlinenutzung gerne als doppelseitige Datei, zum Beispiel um Bilder über zwei Seiten größer und schöner darstellen zu können (Auszug Beispielimmobilie anbei). Für den Druck wird die Datei zudem mit Einzelseiten benötigt.

```html
<!DOCTYPE html>
<html lang="de">
<head>
<meta charset="utf-8">
<title>Exposé Doppelseite – Seite 07/08</title>
<link rel="stylesheet" href="https://fonts.googleapis.com/css2?family=Montserrat:wght@300;400;800;900&display=swap">
<style>
  :root {
    --backdrop: #d9d9d9;
    --paper: #ffffff;
    --anthracite: #262626;
    --accent: #d9452b;
    --brush-tone: rgba(236, 236, 236, 0.85);
    --interior-tone: linear-gradient(160deg, #efe9e0 0%, #c9a79a 45%, #b98a6a 100%);
    --terrace-tone: linear-gradient(180deg, #b9cde0 0%, #dfe3e6 35%, #b8ab9a 70%, #8d7f6d 100%);
    --facade-tone: linear-gradient(180deg, #8aa6d3 0%, #dfe6ef 45%, #f3f3f3 70%, #9c9fae 100%);
  }
  * { margin: 0; padding: 0; box-sizing: border-box; }
  html, body {
    width: 1200px; height: 1200px; overflow: hidden;
    background: var(--backdrop);
    font-family: "Montserrat", sans-serif;
    color: var(--anthracite);
  }
  .spread {
    position: absolute; left: 47px; top: 206px;
    width: 1107px; height: 788px;
    background: var(--paper);
    box-shadow: 0 4px 10px rgba(0,0,0,0.25);
    overflow: hidden;
  }
  .brush-decoration {
    position: absolute; left: 70px; top: 190px;
    width: 760px; height: 575px;
    background:
      radial-gradient(ellipse 28% 48% at 22% 58%, var(--brush-tone) 0%, rgba(236,236,236,0.5) 55%, transparent 100%),
      radial-gradient(ellipse 30% 50% at 72% 45%, var(--brush-tone) 0%, rgba(236,236,236,0.45) 55%, transparent 100%),
      radial-gradient(ellipse 45% 20% at 50% 12%, rgba(238,238,238,0.7) 0%, transparent 100%);
  }
  .section-label {
    position: absolute; top: 29px;
    font-size: 10.5px; font-weight: 900; letter-spacing: 1.2px;
  }
  .section-label--left { left: 37px; }
  .section-label--right { left: 992px; }
  .rule { position: absolute; height: 1px; width: 82px; background: var(--accent); }
  .rule--top-left { left: 35px; top: 47px; }
  .rule--top-right { left: 990px; top: 47px; }
  .rule--foot-left { left: 33px; top: 736px; }
  .rule--foot-right { left: 990px; top: 736px; }
  .page-number {
    position: absolute; top: 743px;
    font-size: 11px; letter-spacing: 1px; font-weight: 400;
  }
  .page-number b { font-weight: 900; }
  .page-number--left { left: 34px; }
  .page-number--right { left: 992px; }

  .photo { position: absolute; }
  .photo--interior { left: 37px; top: 63px; width: 484px; height: 280px; background: var(--interior-tone); }
  .photo--terrace { left: 86px; top: 319px; width: 302px; height: 322px; background: var(--terrace-tone); }
  .photo--facade { left: 498px; top: 366px; width: 540px; height: 348px; background: var(--facade-tone); border: 1px solid #555; }
  .accent-frame {
    position: absolute; left: 202px; top: 366px; width: 270px; height: 217px;
    border: 1.2px solid var(--accent);
  }
  .caption {
    position: absolute; left: 85px; top: 650px; width: 320px;
    font-size: 10.3px; line-height: 12.6px; letter-spacing: 0.9px;
  }
  .caption b, .intro b { font-weight: 900; }

  .headline {
    position: absolute; left: 614px; top: 140px;
    font-size: 55px; line-height: 67px; letter-spacing: 6px;
    text-transform: uppercase;
  }
  .headline span { display: block; font-weight: 900; }
  .headline .headline__light { font-weight: 300; }
  .divider-vertical { position: absolute; width: 1px; background: var(--accent); }
  .divider-vertical--text { left: 846px; top: 165px; height: 163px; }
  .divider-vertical--edge { left: 1072px; top: 68px; height: 632px; }
  .edge-marker { position: absolute; left: 1066px; top: 364px; width: 15px; height: 73px; background: var(--accent); }
  .intro {
    position: absolute; left: 868px; top: 146px; width: 194px;
    font-size: 11.6px; line-height: 14.3px; letter-spacing: 1px;
  }
</style>
</head>
<body>
  <main class="spread">
    <div class="brush-decoration" role="img" aria-label="Dekoration: blasser grauer Pinselstrich im Hintergrund"></div>

    <div class="section-label section-label--left">Inhalt</div>
    <div class="rule rule--top-left"></div>
    <div class="section-label section-label--right">Inhalt</div>
    <div class="rule rule--top-right"></div>

    <div class="photo photo--interior" role="img" aria-label="Foto: offener Wohn- und Essbereich mit Küche, Sofa und Pflanzen"></div>
    <div class="photo photo--terrace" role="img" aria-label="Foto: Dachterrasse mit Blumentopf und Blick auf Wohnhäuser"></div>
    <div class="accent-frame"></div>
    <p class="caption">Lorem <b>ipsum</b> dolor sit amet, consectetuer adipiscing elit, sed diam nonummy nibh euismod tincidunt ut laoreet dolore magna el</p>

    <h1 class="headline">
      <span>Hier</span>
      <span>steht</span>
      <span class="headline__light">Titel</span>
    </h1>
    <div class="divider-vertical divider-vertical--text"></div>
    <p class="intro">Lorem <b>ipsum</b> dolor sit<br>amet, consectetuer<br>adipiscing elit, sed diam<br>nonummy nibh euismod<br>tincidunt ut laoreet<br>dolore magna aliquam<br>erat volutpat. Ut wisi enim<br>ad minim veniam, quis<br>nostrud exerci tation<br>ullamcorper suscipit<br>lobortis nisl ut aliquip ex<br>ea commodo consequat.<br>Duis autem vel</p>

    <div class="photo photo--facade" role="img" aria-label="Foto: weiße Neubaufassade mit Balkonen vor blauem Himmel"></div>
    <div class="divider-vertical divider-vertical--edge"></div>
    <div class="edge-marker"></div>

    <div class="rule rule--foot-left"></div>
    <div class="page-number page-number--left">Seite: <b>07</b></div>
    <div class="rule rule--foot-right"></div>
    <div class="page-number page-number--right">Seite: <b>08</b></div>
  </main>
</body>
</html>
```